Change the world and help build SpinLOOM.tv!

We need a mobile website design for our Beta release - see wireframes attached.
See our Logo design files attached along with fonts, etc.
Please see enclosed .PDF that provides a great overview of our company, LOOM.
Any questions, feel free to ask - we're very engaged here on Sketch Hive and will make ourselves available.
Thanks!
Tobias
Updates
Very pleased with what's coming in! Would like to see some more variety and more volume of designs.
Target Market(s)
Ages 13+ (all genders, races, creeds, income levels, etc)
Coding
Coded - Design and coding required
Number of Pages Required
5+ page
Font styles to use
Colors
Designer to choose colors to be used in the design.
Look and feel
Each slider illustrates characteristics of the customer's brand and the style your logo design should communicate.

```html
<!DOCTYPE html>
<html lang="en">
<head>
<meta charset="utf-8">
<title>SpinLOOM.tv – Thank you</title>
<link rel="stylesheet" href="https://fonts.googleapis.com/css2?family=Lato:wght@400;700&display=swap">
<style>
  :root {
    --navy: #1f2a4a;
    --teal: #4ba3c3;
    --text-grey: #7a7a7a;
    --footer-text: #2e2e2e;
    --page-bg: #ffffff;
  }
  * { margin: 0; padding: 0; box-sizing: border-box; }
  html, body {
    width: 1200px;
    height: 2598px;
    overflow: hidden;
    background: var(--page-bg);
    font-family: "Lato", sans-serif;
  }
  .page {
    position: relative;
    width: 1200px;
    height: 2598px;
  }
  .top-bar {
    position: absolute;
    top: 0; left: 0;
    width: 100%;
    height: 141px;
    background: var(--navy);
  }
  .brand {
    position: absolute;
    top: 224px;
    left: 0;
    width: 100%;
    text-align: center;
  }
  .brand-dot {
    display: block;
    margin: 0 auto 18px;
  }
  .brand-name {
    font-weight: 700;
    font-size: 48px;
    line-height: 56px;
    letter-spacing: 1px;
    color: var(--navy);
  }
  .message {
    position: absolute;
    left: 0;
    width: 100%;
    text-align: center;
    color: var(--text-grey);
  }
  .message-title {
    top: 597px;
    font-weight: 700;
    font-size: 60px;
    line-height: 80px;
  }
  .message-body {
    font-size: 60px;
    line-height: 98px;
  }
  .message-body.intro { top: 783px; }
  .message-body.thanks { top: 1263px; }
  .message-body.signoff { top: 1932px; }
  .site-footer {
    position: absolute;
    top: 2410px;
    left: 0;
    width: 100%;
    height: 44px;
  }
  .footer-link {
    position: absolute;
    top: 0;
    transform: translateX(-50%);
    white-space: nowrap;
    font-size: 33px;
    line-height: 44px;
    color: var(--footer-text);
    text-decoration: none;
  }
</style>
</head>
<body>
<div class="page">
  <header class="top-bar"></header>

  <div class="brand">
    <svg class="brand-dot" width="44" height="44" viewBox="0 0 44 44" aria-hidden="true">
      <circle cx="22" cy="22" r="20" fill="var(--teal)"/>
    </svg>
    <div class="brand-name">SPINLOOM.TV</div>
  </div>

  <h1 class="message message-title">Thank you for your interest!</h1>

  <p class="message message-body intro">
    Please check your email for<br>
    information about how our Beta<br>
    program will work and what you<br>
    can expect along the way.
  </p>

  <p class="message message-body thanks">
    We’re so excited to have you on<br>
    the LOOM Team! You’re doing a<br>
    wonderful thing for the world,<br>
    and we are forever grateful for<br>
    you!
  </p>

  <p class="message message-body signoff">
    With love,<br>
    - Marisa &amp; Tobias
  </p>

  <footer class="site-footer">
    <a class="footer-link" href="#" style="left:195px">Terms and Condition</a>
    <a class="footer-link" href="#" style="left:529px">Privacy Policy</a>
    <a class="footer-link" href="#" style="left:781px">About LOOM</a>
    <a class="footer-link" href="#" style="left:1041px">The LOOM Team</a>
  </footer>
</div>
</body>
</html>
```